fernbolt website

commerce website to sell cookeries, brackets, mailboxes and to show off homes built. Modern Steel in design see kelvo rides web page to be like: https://www.kelvorides.com/en/ sorry its blue mantis hosting word press divi

must be able to add products to page

Target Market(s)

mainly western states of U.S.

Industry/Entity Type

Building Product

Coding

Coded - Design and coding required

Number of Pages Required

3 page

Font styles to use
Sans Serif

Colors

Designer to choose colors to be used in the design.

Requirements
Must have
• customers to be able to order products from page
• blue mantis hosting word press divi

```html
<!DOCTYPE html>
<html lang="en">
<head>
<meta charset="utf-8">
<title>Fernbolt – Modern Steel Design</title>
<link rel="stylesheet" href="https://fonts.googleapis.com/css2?family=Roboto:wght@300;400;500;700&display=swap">
<style>
:root{
  --brand:#4a6491;
  --button:#46608d;
  --accent:#f9b65a;
  --ink:#1a1a1a;
  --muted:#555;
  --bar:#e6e6e6;
  --tile:#f3f3f3;
  --dark:#222222;
  --footer:#0f0f0f;
  --gold:#f5b50a;
  --white:#fff;
}
*{box-sizing:border-box;margin:0;padding:0}
html,body{width:1200px;height:2506px;overflow:hidden}
body{font-family:"Roboto",sans-serif;color:var(--ink);background:var(--white);position:relative}
a{color:inherit;text-decoration:none}
.section{position:absolute;left:0;width:1200px}

/* header */
.topbar{top:0;height:65px;background:var(--brand)}
.brand{position:absolute;left:166px;top:18px;color:var(--white);font-size:17px;font-weight:500;letter-spacing:.5px;display:flex;align-items:center;gap:8px}
.brand-mark{width:14px;height:14px;background:var(--white);border-radius:50%}
.search{position:absolute;left:386px;top:12px;width:345px;height:38px;background:var(--white);border-radius:3px;overflow:hidden}
.search span{position:absolute;left:13px;top:13px;font-size:11px;color:#333}
.search .search-btn{position:absolute;right:0;top:0;width:38px;height:38px;background:var(--accent)}
.account{position:absolute;left:877px;top:20px;color:var(--white);font-size:13px;font-weight:500;display:flex;align-items:center;gap:5px}
.cart{position:absolute;left:998px;top:18px;color:var(--white);font-size:11px;display:flex;align-items:center;gap:4px}

.infobar{top:65px;height:38px;background:var(--bar);font-size:13px;color:#333}
.infobar .promo{position:absolute;left:158px;top:12px}
.infobar .promo a{color:var(--brand);text-decoration:underline;font-weight:500}
.mainnav{position:absolute;right:159px;top:12px;display:flex;gap:22px;color:#111}

/* hero */
.hero{top:103px;height:517px;overflow:hidden}
.hero-photo{position:absolute;inset:0;background:linear-gradient(100deg,#2a3340 0%,#3b4a66 45%,#4d5e7c 65%,#2f3a2c 100%)}
.hero-overlay{position:absolute;inset:0}
.hero-copy{position:absolute;left:160px;top:155px;color:var(--white);width:380px}
.hero-copy h1{font-weight:400;font-size:60px;line-height:60px}
.hero-copy h1 b{font-weight:500;display:block}
.hero-copy p{font-size:14.5px;line-height:19px;margin-top:14px;width:360px}
.btn{display:inline-block;background:var(--button);color:var(--white);font-weight:500;text-align:center}
.hero-copy .btn{margin-top:18px;width:112px;height:45px;line-height:45px;font-size:14px}
.dots{position:absolute;display:flex;gap:8px}
.dots i{width:7px;height:7px;border-radius:50%;background:var(--white)}
.dots i:first-child{background:var(--accent)}

/* offers */
.offers{top:675px;height:322px}
.offer{position:absolute;top:0;width:284px;height:322px;background:var(--tile)}
.offer small{position:absolute;left:12px;top:20px;font-size:13px;font-weight:500}
.offer h2{position:absolute;left:12px;top:35px;font-size:23px;font-weight:500}
.offer .shot{position:absolute;left:10px;top:70px;width:265px;height:188px;border:1px solid #ddd}
.offer .btn{position:absolute;left:10px;top:260px;width:265px;height:46px;line-height:46px;font-size:14px;letter-spacing:.5px}

/* top sellers */
.sellers{top:1043px;height:544px;background:var(--dark)}
.sellers h2{position:absolute;top:57px;width:100%;text-align:center;color:var(--white);font-size:34px;font-weight:500}
.product{position:absolute;top:122px;width:210px;height:328px;background:var(--white);text-align:center}
.product .shot{margin:18px auto 0;width:160px;height:125px}
.stars{color:var(--gold);font-size:13px;letter-spacing:1px}
.product .stars{margin-top:28px}
.product h3{font-size:18px;font-weight:500;margin-top:1px}
.product p{font-size:13.5px;color:var(--muted);line-height:16.5px;padding:0 12px;margin-top:4px}
.product .btn{margin-top:10px;width:90px;height:35px;line-height:35px;font-size:12.5px}
.badge{position:absolute;right:8px;top:4px;width:42px;height:42px;border-radius:50%;background:var(--accent);font-size:9px;line-height:10px;padding-top:11px;text-align:center}

/* reviews */
.reviews{top:1620px;height:440px}
.reviews h2{position:absolute;top:35px;width:100%;text-align:center;font-size:34px;font-weight:500}
.review{position:absolute;top:103px;width:284px;height:246px;background:var(--white);box-shadow:1px 2px 4px rgba(0,0,0,.25);text-align:center}
.review .quote{margin-top:18px;font-size:44px;line-height:34px;color:#bbb;font-family:Georgia,serif}
.review h3{font-size:17px;font-weight:400;margin-top:2px}
.review time{display:block;font-size:13px;color:var(--muted);margin-top:3px}
.review .stars{margin-top:6px;font-size:14px}
.review p{font-size:14px;line-height:18px;padding:0 20px;margin-top:8px}
.reviews .more{position:absolute;left:543px;top:380px;width:113px;height:46px;line-height:46px;font-size:14px}

/* footer */
.footer{top:2108px;height:398px;background:var(--footer);color:var(--white)}
.footer-brand{position:absolute;left:160px;top:85px;font-size:26px;font-weight:500;display:flex;align-items:center;gap:10px}
.footer-brand .brand-mark{width:22px;height:22px}
.copyright{position:absolute;left:158px;top:223px;font-size:13px;line-height:19px}
.col{position:absolute;top:115px}
.col h4{font-size:17px;font-weight:400;letter-spacing:.4px}
.col ul{list-style:none;margin-top:18px;font-size:14px}
.col li{height:33px}
.payments{position:absolute;left:446px;top:328px;display:flex;gap:2px}
.payments span{width:43px;height:29px;background:#e9e9e9;color:#333;font-size:9px;font-weight:500;display:flex;align-items:center;justify-content:center;border-radius:2px}
</style>
</head>
<body>

<header class="section topbar">
  <a class="brand" href="#"><span class="brand-mark"></span>fernbolt</a>
  <div class="search"><span>Search Products</span>
    <div class="search-btn"><svg width="38" height="38" viewBox="0 0 38 38"><circle cx="18" cy="18" r="5.5" fill="none" stroke="#333" stroke-width="2"/><line x1="22" y1="22" x2="26" y2="26" stroke="#333" stroke-width="2"/></svg></div>
  </div>
  <a class="account" href="#"><svg width="13" height="11" viewBox="0 0 13 11"><rect x="1" y="3" width="11" height="7" fill="none" stroke="#fff" stroke-width="1.4"/><line x1="6.5" y1="0" x2="6.5" y2="7" stroke="#fff" stroke-width="1.4"/></svg>Sign In Now</a>
  <a class="cart" href="#"><svg width="18" height="16" viewBox="0 0 18 16"><path d="M1 2h3l2 8h9l2-6H5" fill="none" stroke="#fff" stroke-width="1.4"/><circle cx="7" cy="13.5" r="1.4" fill="#fff"/><circle cx="14" cy="13.5" r="1.4" fill="#fff"/></svg>Cart</a>
</header>

<div class="section infobar">
  <p class="promo">FREE SHIPPING ON ORDERS OVER $50. <a href="#">Terms &amp; Conditions apply</a></p>
  <nav class="mainnav"><a href="#">Home</a><span>I</span><a href="#">Products</a><span>I</span><a href="#">Contact us</a></nav>
</div>

<section class="section hero">
  <div class="hero-photo" role="img" aria-label="Modern steel-clad building with dark vertical panels under a blue sky, trees at the edges"></div>
  <svg class="hero-overlay" width="1200" height="517" viewBox="0 0 1200 517">
    <polygon points="0,0 112,0 575,215 490,517 0,517" fill="#15171c" opacity=".78"/>
    <polyline points="112,0 575,215 490,517" fill="none" stroke="#f9b65a" stroke-width="5"/>
    <polyline points="140,253 130,263 140,273" fill="none" stroke="#fff" stroke-width="2.5"/>
    <polyline points="1055,253 1065,263 1055,273" fill="none" stroke="#fff" stroke-width="2.5"/>
  </svg>
  <div class="hero-copy">
    <h1>Modern<b>Steel Design</b></h1>
    <p>Many desktop publishing packages and web page editors now use Lorem Ipsum as their default model text, and a search for 'lorem ipsum will uncover many web sites . . .</p>
    <a class="btn" href="#">View More</a>
  </div>
  <div class="dots" style="left:158px;top:462px"><i></i><i></i><i></i></div>
</section>

<section class="section offers">
  <article class="offer" style="left:159px"><small>Up to 50% off:</small><h2>Steel Cookery</h2>
    <div class="shot" role="img" aria-label="Stainless steel kitchen appliances" style="background:radial-gradient(ellipse at center,#b9bcbf 0%,#e4e5e6 45%,#fff 75%)"></div>
    <a class="btn" href="#">ORDER NOW</a></article>
  <article class="offer" style="left:458px"><small>Up to 50% off:</small><h2>Brackets</h2>
    <div class="shot" role="img" aria-label="Perforated galvanised angle brackets" style="background:radial-gradient(ellipse at center,#a9adb1 0%,#dcdee0 45%,#fff 75%)"></div>
    <a class="btn" href="#">ORDER NOW</a></article>
  <article class="offer" style="left:757px"><small>Up to 50% off:</small><h2>Mailboxes</h2>
    <div class="shot" role="img" aria-label="Grey steel mailbox on a post" style="background:radial-gradient(ellipse at center,#9a9c9f 0%,#d6d7d8 40%,#fff 70%)"></div>
    <a class="btn" href="#">ORDER NOW</a></article>
</section>

<section class="section sellers">
  <h2>Top Sell Products</h2>
  <svg width="1200" height="544" viewBox="0 0 1200 544" style="position:absolute;left:0;top:0">
    <polyline points="141,284 131,294 141,304" fill="none" stroke="#fff" stroke-width="3"/>
    <polyline points="1055,284 1065,294 1055,304" fill="none" stroke="#fff" stroke-width="3"/>
  </svg>
  <article class="product" style="left:159px"><div class="shot" role="img" aria-label="Steel corner brackets" style="background:radial-gradient(ellipse,#b4b7ba 0%,#fff 70%)"></div>
    <div class="stars">★★★★</div><h3>Contrary to popular</h3><p>There are many variations of passages of Lorem Ipsum available</p><a class="btn" href="#">Order Now</a></article>
  <article class="product" style="left:383px"><div class="badge">-10%<br>Off</div><div class="shot" role="img" aria-label="Stainless steel cooking pot with lid" style="background:radial-gradient(ellipse,#9ea1a5 0%,#fff 70%)"></div>
    <div class="stars">★★★★★</div><h3>Contrary to popular</h3><p>There are many variations of passages of Lorem Ipsum available</p><a class="btn" href="#">Order Now</a></article>
  <article class="product" style="left:608px"><div class="shot" role="img" aria-label="Two flat steel mounting plates" style="background:radial-gradient(ellipse,#c9cbcd 0%,#fff 65%)"></div>
    <div class="stars">★★★★★</div><h3>Contrary to popular</h3><p>There are many variations of passages of Lorem Ipsum available</p><a class="btn" href="#">Order Now</a></article>
  <article class="product" style="left:833px"><div class="badge">-10%<br>Off</div><div class="shot" role="img" aria-label="Steel saucepan with long handle and lid" style="background:radial-gradient(ellipse,#8f9296 0%,#fff 70%)"></div>
    <div class="stars">★★★★★</div><h3>Contrary to popular</h3><p>There are many variations of passages of Lorem Ipsum available</p><a class="btn" href="#">Order Now</a></article>
  <div class="dots" style="left:573px;top:488px"><i></i><i></i><i></i><i></i></div>
</section>

<section class="section reviews">
  <h2>Customer Review</h2>
  <article class="review" style="left:159px"><div class="quote">“</div><h3>JOHN DOE</h3><time>jan 31,2020</time><div class="stars">★★★★★</div>
    <p>All the Lorem Ipsum generators on the Internet tend to repeat predefined chunks as necessary, making this the first true generator</p></article>
  <article class="review" style="left:458px"><div class="quote">“</div><h3>JOHN DOE</h3><time>jan 31,2020</time><div class="stars">★★★★★</div>
    <p>All the Lorem Ipsum generators on the Internet tend to repeat predefined chunks as necessary, making this the first true generator</p></article>
  <article class="review" style="left:757px"><div class="quote">“</div><h3>JOHN DOE</h3><time>jan 31,2020</time><div class="stars">★★★★★</div>
    <p>All the Lorem Ipsum generators on the Internet tend to repeat predefined chunks as necessary, making this the first true generator</p></article>
  <a class="btn more" href="#">View More</a>
</section>

<footer class="section footer">
  <div class="footer-brand"><span class="brand-mark"></span>fernbolt</div>
  <p class="copyright">Copyright©2020 Fernbolt.<br>All Rights Reserved.</p>
  <div class="col" style="left:415px"><h4>CONNECT</h4><ul><li>Linkwall</li><li>Chirpline</li><li>Photoloop</li></ul></div>
  <div class="col" style="left:588px"><h4>QUICK LINK</h4><ul><li>Home</li><li>Products</li><li>Contact</li></ul></div>
  <div class="col" style="left:754px"><h4>PRODUCT</h4><ul><li>Cookery</li><li>Brackets</li><li>Mailboxes</li></ul></div>
  <div class="col" style="left:916px"><h4>INFORMATION</h4><ul><li>Use &amp; Care</li><li>Shipping &amp; Handling</li><li>Warranty &amp; Returns</li><li>Customer Care</li></ul></div>
  <div class="payments"><span>Orbipay</span><span>Tallo</span><span>Quenza</span><span>Pavo</span><span>Lumen</span><span>Cirra</span><span>Brisk</span></div>
</footer>

</body>
</html>
```